DuePoint.com website design

We are a collection agency that collects debt from past residents of apartments on behalf of Property Management Companies. We are want to design a 3 page website with - Home - How it Works - Schedule Demo. We'd like a sketch of a skyline showing high rise apartment buildings, houses, shops, etc. We would like for there to be some animation, possibly clouds and the sun slowly moving. Maybe kids playing ball or catch or something like that. Bird flying and landing. An electric car charging (to indicate we are modern). We are looking for a friendly community vibe. The site will also need a button "Property Managers Login". When some comes to the site we would like a pop up that says "Property Managers Click Here/Past Residents Click Here" with a different icon for each that relates to the description. I've included a link to a test site we had designed so feel free to use some of the copy from it. We just aren't happy with the design. On the Home page our tag line should be "Get more payments, faster, from past residents!" and "Digital First, NOT Digital Only". All without transaction fees, we don't get paid unless we get you paid first!
Additional selling points:

24 hour virtual agent and virtual telephone agent so we don't miss any opportunities to GET YOUR MONEY!

Old school collection strategies meet cutting edge technology to create effective work flow algorithms to put the best debt collectors on your accounts with data driven intelligence to determine the best way to get paid.

No Subscription Fees
No Payment Processing Fees
No Software Fees
No Mail, Email or TXT Fees

Inquire about our FIRST PARTY accounts receivable outsourcing. You may qualify for free post move out A/R processing and AI payment negotiator for the low hanging fruit. Don't pay full collection commission when there wasn't a full collection attempt!

For the How it Works page - See the page from our previous design. I will include the link below. Please come up with your own version of this but you can use the copy from this page.

The schedule demo page will be a form that will feed to our CRM that will include:
Name
Email
Company
Title
Phone Number
Number of Units
Tell us how we can help you: (a box for them provide details)

Also include our phone number at the bottom with something like

Here is a link to our previous design test site:
https://brelmora-preview.example/duepoint-new/
I've attached an image of the back end so you can get an idea of the colors we need, I've also included our logo. For the most part we would like most of the site to match the blue colors from our logo, but we do need to incorporate some of the yellow in the images I've attached. Possibly make the buttons on the site the yellow color? Make the sun Match the yellow? I'll leave it up to you.

```html
<!DOCTYPE html>
<html lang="en">
<head>
<meta charset="utf-8">
<title>DuePoint — Debt Recovery Management</title>
<link href="https://fonts.googleapis.com/css2?family=Lato:wght@300;400;700;900&display=swap" rel="stylesheet">
<style>
:root{
  --navy:#0f3b6e;
  --teal:#1fb5d4;
  --ink:#111a2e;
  --dark:#222222;
  --dark-card:#2f2f2f;
  --cream:#fdf5e1;
  --sun:#fde6b4;
  --yellow:#fbbf4a;
  --peach:#fcc27a;
  --muted:#8e97ae;
  --light-bg:#f7f7f8;
  --line-light:#ececee;
  --white:#ffffff;
}
*{margin:0;padding:0;box-sizing:border-box}
html,body{width:1200px;height:3518px;overflow:hidden}
body{font-family:'Lato',sans-serif;color:var(--ink);background:var(--white);position:relative}
a{color:inherit;text-decoration:none}

/* header */
.site-header{position:absolute;top:0;left:0;width:1200px;height:90px;z-index:5}
.brand{position:absolute;left:87px;top:22px;display:flex;align-items:center;gap:10px;font-weight:900;font-size:27px;color:var(--navy)}
.brand-mark{width:30px;height:30px;background:var(--navy);border-radius:6px}
.main-nav{position:absolute;top:34px;font-size:13px;color:var(--muted)}
.main-nav.active{color:var(--ink);font-weight:700}
.btn-outline{position:absolute;border:1.5px solid var(--navy);color:var(--navy);font-size:13px;display:flex;align-items:center;justify-content:center;background:var(--white)}
.btn-solid{position:absolute;background:var(--navy);color:var(--white);font-size:13px;display:flex;align-items:center;justify-content:center}

/* hero */
.hero{position:absolute;top:0;left:0;width:1200px;height:765px;overflow:hidden;background:var(--white)}
.hero-glow{position:absolute;left:95px;top:95px;width:1010px;height:1010px;border-radius:50%;background:var(--cream)}
.hero-sun{position:absolute;left:352px;top:470px;width:496px;height:496px;border-radius:50%;background:var(--sun)}
.hero-title{position:absolute;top:182px;left:0;width:1200px;text-align:center;font-weight:700;font-size:46px;line-height:53px;letter-spacing:-.5px;color:var(--ink)}
.hero-sub{position:absolute;top:312px;left:0;width:1200px;text-align:center;font-size:13.5px;line-height:23px;color:var(--muted)}
.skyline{position:absolute;left:0;top:350px;width:1200px;height:415px;
  background:linear-gradient(180deg,rgba(31,181,212,0) 0%,rgba(31,181,212,.35) 22%,rgba(15,59,110,.75) 45%,#1c2a3d 65%,#222 85%)}

/* dark section */
.dark-band{position:absolute;left:0;top:765px;width:1200px;height:687px;background:var(--dark)}
.vline{position:absolute;top:0;width:1px;height:100%;background:rgba(255,255,255,.06)}
.pitch{position:absolute;left:83px;top:833px;width:690px;font-size:38px;line-height:53px;color:var(--white);font-weight:400;letter-spacing:-.4px}
.pitch strong{color:var(--yellow);font-weight:700}
.pitch-side{position:absolute;left:797px;top:856px;width:320px;font-size:13.5px;line-height:23.5px;color:#d6d6d6}
.features{position:absolute;left:83px;top:1103px;width:1032px;height:280px;background:var(--dark-card)}
.feature{position:absolute;top:1103px;width:258px;height:280px;padding:40px 27px;color:var(--white)}
.feature .num{font-size:25px;color:#bdbdbd;font-weight:400;margin-bottom:18px}
.feature .title{font-size:19px;line-height:27px}
.feature.is-active{top:1077px;height:306px;background:var(--white);color:var(--ink)}
.feature.is-active .num{color:#6c6c6c}
.feature .desc{font-size:13.5px;line-height:18px;color:#6e6e6e;margin-top:20px}
.feature .more{margin-top:30px;font-size:15px;font-weight:700;display:flex;align-items:center;gap:10px;letter-spacing:.3px}

/* services */
.services{position:absolute;left:0;top:1452px;width:1200px;height:1001px;background:var(--white)}
.services .vline{background:var(--line-light)}
.sec-title{position:absolute;font-size:40px;line-height:54px;font-weight:400;letter-spacing:-.5px;color:var(--ink)}
.sec-text{position:absolute;font-size:13.5px;line-height:23.5px;color:var(--muted)}
.photo{position:absolute}

/* testimonials */
.testimonials{position:absolute;left:0;top:2453px;width:1200px;height:670px;background:var(--light-bg);overflow:hidden}
.testimonials h2{position:absolute;top:88px;left:0;width:1200px;text-align:center;font-size:40px;font-weight:400;letter-spacing:-.5px}
.review{position:absolute;top:191px;width:414px;height:300px;background:var(--white);padding:40px 40px}
.review .quote{font-family:Georgia,serif;font-size:48px;font-weight:700;line-height:30px;color:var(--ink)}
.review .when{position:absolute;right:40px;top:42px;font-size:13px;color:var(--muted)}
.review p{margin-top:20px;font-size:12.5px;line-height:27px;color:#333}
.review .foot{position:absolute;left:40px;right:40px;bottom:40px;border-top:1px solid #eee;padding-top:22px;display:flex;align-items:center;gap:11px;font-size:13px}
.avatar{width:32px;height:32px;border-radius:50%;background:#b7a49a}
.review .like{margin-left:auto}
.progress{position:absolute;left:516px;top:566px;width:167px;height:3px;background:#e3e3e6}
.progress span{display:block;width:40px;height:3px;background:var(--navy)}
.arrow-btn{position:absolute;top:546px;width:40px;height:40px;display:flex;align-items:center;justify-content:center;border:1.5px solid var(--navy)}

/* footer */
.site-footer{position:absolute;left:0;top:3123px;width:1200px;height:395px;background:#1f1f1f;color:var(--white)}
.footer-brand{position:absolute;left:91px;top:100px;display:flex;align-items:center;gap:14px;font-size:44px;font-weight:900}
.footer-brand .brand-mark{width:56px;height:56px;background:var(--white);border-radius:10px}
.footer-pitch{position:absolute;left:553px;top:84px;width:560px;font-size:19px;line-height:28px;color:#d8d8d8;text-transform:uppercase;font-weight:400}
.footer-tag{position:absolute;left:553px;top:160px;font-size:19px;font-weight:700}
.footer-nav{position:absolute;top:249px;font-size:13px}
.footer-cta{position:absolute;left:553px;top:236px;width:114px;height:40px;background:var(--peach);color:var(--ink);font-size:13px;display:flex;align-items:center;justify-content:center}
.social{position:absolute;top:236px;width:40px;height:40px;border:1.5px solid #ddd;display:flex;align-items:center;justify-content:center}
.social i{width:12px;height:12px;border-radius:50%;background:#ddd}
.footer-rule{position:absolute;left:83px;top:317px;width:1032px;height:1px;background:#444}
.copyright{position:absolute;top:340px;left:0;width:1200px;text-align:center;font-size:13.5px;color:#cfcfcf}
.copyright b{font-weight:400;color:var(--white)}
</style>
</head>
<body>

<section class="hero">
  <div class="hero-glow"></div>
  <div class="hero-sun"></div>
  <div class="skyline" role="img" aria-label="City skyline illustration with teal, navy and dark high-rise apartment buildings in front of a rising yellow sun"></div>
  <h1 class="hero-title">Get more payments, faster, from past residents!<br>Digital First, NOT Digital Only</h1>
  <p class="hero-sub">All without transaction fees, we don't get paid unless we get you paid first!<br>24 hour virtual agent and virtual telephone agent so we don't miss any opportunities to GET YOUR MONEY!</p>
  <a class="btn-solid" style="left:418px;top:410px;width:173px;height:50px;font-size:14px">Get Started Now</a>
  <a class="btn-outline" style="left:612px;top:410px;width:169px;height:50px;font-size:14px">Start Free Demo</a>
</section>

<header class="site-header">
  <div class="brand"><span class="brand-mark"></span>DuePoint</div>
  <a class="main-nav active" style="left:485px">Home</a>
  <a class="main-nav" style="left:553px">How It Works</a>
  <a class="main-nav" style="left:663px">About US</a>
  <a class="main-nav" style="left:752px">Contact</a>
  <a class="btn-outline" style="left:830px;top:22px;width:83px;height:38px">Login</a>
  <a class="btn-solid" style="left:924px;top:22px;width:191px;height:38px">Property Managers Login</a>
</header>

<section class="dark-band">
  <div class="vline" style="left:67px"></div>
  <div class="vline" style="left:423px"></div>
  <div class="vline" style="left:541px"></div>
  <div class="vline" style="left:777px"></div>
  <div class="vline" style="left:1132px"></div>
</section>
<h2 class="pitch">24 hour virtual agent and virtual telephone agent so we don't miss any opportunities to <strong>GET YOUR MONEY!</strong></h2>
<p class="pitch-side">Old school collection strategies meet cutting edge technology to create effective work flow algorithms to put the best debt collectors on your accounts with data driven intelligence to determine the best way to get paid.</p>

<div class="features"></div>
<div class="feature" style="left:83px"><div class="num">01</div><div class="title">No Subscription<br>Fees</div></div>
<div class="feature" style="left:341px"><div class="num">02</div><div class="title">No Payment<br>Processing Fees</div></div>
<div class="feature is-active" style="left:600px">
  <div class="num">03</div><div class="title">No Software<br>Fees</div>
  <div class="desc">Lorem ipsum dolor sit amet, consectetur adipiscing elit. Nam lorem mi vitae ipsum vel.</div>
  <div class="more">LEARN MORE
    <svg width="9" height="14" viewBox="0 0 9 14"><path d="M2 1l6 6-6 6" fill="none" stroke="#111a2e" stroke-width="1.6"/></svg>
  </div>
</div>
<div class="feature" style="left:857px"><div class="num">04</div><div class="title">No Mail, Email<br>or TXT Fees</div></div>

<section class="services">
  <div class="vline" style="left:67px"></div>
  <div class="vline" style="left:423px"></div>
  <div class="vline" style="left:541px"></div>
  <div class="vline" style="left:777px"></div>
  <div class="vline" style="left:1132px"></div>

  <h2 class="sec-title" style="left:83px;top:126px">Debt Collection<br>Services Made Simple</h2>
  <p class="sec-text" style="left:83px;top:245px;width:490px">DuePoint provides you with complete access to what is happening with your accounts. Our reports, payment processing and account management leaves you without questions about what is being done to get you paid!</p>
  <a class="btn-solid" style="left:83px;top:369px;width:140px;height:48px;font-size:14px">Learn More</a>
  <div class="photo" style="left:658px;top:84px;width:457px;height:374px;background:linear-gradient(180deg,#cfd0d2,#9a9c9f)" role="img" aria-label="Photo of two businessmen in suits shaking hands across a desk"></div>

  <div class="photo" style="left:83px;top:542px;width:458px;height:374px;background:linear-gradient(180deg,#e9e9e7,#8a8c90)" role="img" aria-label="Photo of two smiling businesswomen standing with arms crossed in an office"></div>
  <h2 class="sec-title" style="left:625px;top:561px">Proven Debt Recovery<br>For Apartment Managers</h2>
  <p class="sec-text" style="left:625px;top:700px;width:490px">Our CEO, Dale Harlow, founded one of the first nationwide Multifamily collection agencies in 1998. It would be hard to find more experience at collecting for apartment owners. Now we have taken that experience and modernized it with intelligent data driven algorithms coupled with no nonsense collection strategies to get you paid MORE, QUICKER.</p>
  <a class="btn-solid" style="left:625px;top:849px;width:139px;height:50px;font-size:14px">Learn More</a>
</section>

<section class="testimonials">
  <h2>What Our People Say</h2>
  <article class="review" style="left:83px">
    <div class="quote">“</div><span class="when">a day ago</span>
    <p>Lorem ipsum dolor sit amet, consectetur adipiscing elit. Tristique nisl vulputate amet enim urna, nibh arcu, nam sagittis. Justo, amet placerat fermentum faucibus. Placerat sed in tincidunt id senectus feugiat enim.</p>
    <div class="foot"><span class="avatar"></span>Mirela Toskan
      <svg class="like" width="18" height="18" viewBox="0 0 18 18"><path d="M2 8h3v8H2zM5 8l4-6c1.5 0 2 1 1.7 2.3L10 7h5c1 0 1.5.8 1.3 1.7l-1.3 6c-.2.8-.8 1.3-1.6 1.3H5" fill="none" stroke="#111a2e" stroke-width="1.3"/></svg>
    </div>
  </article>
  <article class="review" style="left:516px">
    <div class="quote">“</div><span class="when">2 days ago</span>
    <p>Lorem ipsum dolor sit amet, consectetur adipiscing elit. Tristique nisl vulputate amet enim urna, nibh arcu, nam sagittis. Justo, amet placerat fermentum faucibus. Placerat sed in tincidunt id senectus feugiat enim.</p>
    <div class="foot"><span class="avatar" style="background:#c49a86"></span>Rowan Bellamy Okafor
      <svg class="like" width="18" height="18" viewBox="0 0 18 18"><path d="M2 8h3v8H2zM5 8l4-6c1.5 0 2 1 1.7 2.3L10 7h5c1 0 1.5.8 1.3 1.7l-1.3 6c-.2.8-.8 1.3-1.6 1.3H5" fill="none" stroke="#111a2e" stroke-width="1.3"/></svg>
    </div>
  </article>
  <article class="review" style="left:950px">
    <div class="quote">“</div>
    <p>Lorem ipsum dolor sit amet, consectetur adipiscing elit. Tristique nisl vulputate amet enim urna, nibh arcu, nam sagittis. Justo, amet placerat fermentum faucibus. Placerat sed in tincidunt id senectus feugiat enim.</p>
    <div class="foot"><span class="avatar" style="background:#5a4a44"></span>Tessa Whitcombe</div>
  </article>
  <div class="progress"><span></span></div>
  <a class="arrow-btn" style="left:1022px;background:var(--white)"><svg width="9" height="14" viewBox="0 0 9 14"><path d="M7 1L1 7l6 6" fill="none" stroke="#0f3b6e" stroke-width="1.5"/></svg></a>
  <a class="arrow-btn" style="left:1075px;background:var(--navy)"><svg width="9" height="14" viewBox="0 0 9 14"><path d="M2 1l6 6-6 6" fill="none" stroke="#fff" stroke-width="1.5"/></svg></a>
</section>

<footer class="site-footer">
  <div class="footer-brand"><span class="brand-mark"></span>DuePoint</div>
  <p class="footer-pitch">Let DuePoint earn your business, if we don't get you paid we don't charge you anything</p>
  <p class="footer-tag">We Want To Earn Your Business</p>
  <a class="footer-nav" style="left:83px">Home</a>
  <a class="footer-nav" style="left:172px">How It Works</a>
  <a class="footer-nav" style="left:303px">Schedule Demo</a>
  <a class="footer-nav" style="left:444px">About US</a>
  <a class="footer-cta">Contact Us</a>
  <a class="social" style="left:916px" aria-label="Social profile 1"><i></i></a>
  <a class="social" style="left:970px" aria-label="Social profile 2"><i></i></a>
  <a class="social" style="left:1023px" aria-label="Social profile 3"><i></i></a>
  <a class="social" style="left:1075px" aria-label="Social profile 4"><i></i></a>
  <div class="footer-rule"></div>
  <p class="copyright">©2022 All rights reserved by <b>DuePoint</b> &nbsp;•&nbsp; Privacy Policy &nbsp;•&nbsp; Term Conditions</p>
</footer>

</body>
</html>
```